SEAFOOD PACKAGING (Products for consumer)

We are looking to create packaging for various seafood products such as octopus and squid. We plan to sell our products in upscale supermarkets.

We are specializing in cut octopus this time.

Please include our company logo. Also, please leave a transparent area so that customers can see the product inside.
Updates

We want to show what is inside, so a picture of the octopus is not required. We need something simple and sophisticated.

Target Market(s)

upscale store in US and ASIA

Industry/Entity Type

Fisheries dealer

Requirements
Must have
• Please include the attached logo,Blue one is preferred.Please leave a transparent part so that the contents of the product can be seen by the consumer.1. product name on packaging →CUT OCTOPUS,TAKO SASHIMI,Highest quality,Top quality etc... 3. What text information should be on the packaging →(It may be edited, but this is the image) The raw materials are caught in a very clean environment and processed in a modern factory with KVT certification. We are committed to additive-free products. 4. Packing size(cm/inch)→it will be about 19cm*22cm. 5. what kind of packaging do you use →PP or PA 6. dll →ai,jag
Nice to have
• https://plenvik.com/shots/4829173-Merulo-Prawn We need something simple and sophisticated like this one.
Should not have
• We want to show what is inside, so a picture of the octopus is not required. We need something simple and sophisticated.

```html
<!DOCTYPE html>
<html lang="en">
<head>
<meta charset="utf-8">
<title>Cut Octopus – Tako Sashimi Package</title>
<link href="https://fonts.googleapis.com/css2?family=Oswald:wght@700&family=Barlow+Condensed:wght@500;600&family=Josefin+Sans:wght@600&family=Barlow:wght@700&display=swap" rel="stylesheet">
<style>
  :root {
    --navy: #25339a;
    --blue: #4a5fb0;
    --blue-light: #6e80c2;
    --red: #b0262e;
    --red-soft: #d0656a;
    --film: #f2f3f5;
    --seal: #e6e8ec;
    --tray: #16171c;
    --backdrop: #ffffff;
  }
  * { box-sizing: border-box; margin: 0; padding: 0; }
  html, body { width: 1200px; height: 1200px; overflow: hidden; background: var(--backdrop); }
  .canvas { position: relative; width: 1200px; height: 1200px; }
  .pack {
    position: absolute; left: 232px; top: 160px; width: 746px; height: 865px;
    background: var(--film); overflow: hidden;
  }
  .seal {
    position: absolute; left: 0; width: 100%; height: 48px;
    background: repeating-linear-gradient(90deg, var(--seal) 0 3px, #f7f8fa 3px 6px);
  }
  .seal--top { top: 0; }
  .seal--bottom { bottom: 0; }
  .brand-tab {
    position: absolute; left: 318px; top: 0; width: 108px; height: 168px;
    background: var(--navy);
    display: flex; flex-direction: column; align-items: center; justify-content: flex-end;
    padding-bottom: 22px; gap: 10px;
  }
  .brand-tab__dot { width: 18px; height: 18px; border-radius: 50%; background: #fff; }
  .brand-tab__name {
    font-family: "Barlow", sans-serif; font-weight: 700; font-size: 22px;
    letter-spacing: 2px; color: #fff;
  }
  .title {
    position: absolute; left: 102px; top: 84px;
    font-family: "Oswald", sans-serif; font-weight: 700; line-height: 1;
    color: var(--navy);
  }
  .title__line {
    display: block; font-size: 128px; letter-spacing: -2px;
    background: linear-gradient(180deg, var(--navy) 0%, var(--blue) 55%, var(--blue-light) 100%);
    -webkit-background-clip: text; background-clip: text; color: transparent;
    filter: drop-shadow(5px 3px 0 var(--red-soft));
  }
  .title__line + .title__line { margin-top: -10px; }
  .subtitle {
    position: absolute; left: 104px; top: 340px;
    font-family: "Josefin Sans", sans-serif; font-weight: 600; font-size: 37px;
    letter-spacing: 7px; color: var(--red);
  }
  .claim {
    position: absolute; left: 104px; top: 390px; width: 400px;
    font-family: "Barlow Condensed", sans-serif; font-weight: 600; font-size: 14.5px;
    line-height: 19px; text-transform: uppercase; color: var(--red);
  }
  .benefit-band {
    position: absolute; left: 0; top: 465px; width: 600px; height: 47px;
    background: var(--navy);
    display: flex; align-items: center; padding-left: 98px;
    font-family: "Barlow", sans-serif; font-weight: 700; font-size: 21px;
    color: #fff; white-space: nowrap;
  }
  .window {
    position: absolute; left: 43px; top: 512px; width: 663px; height: 303px;
    background: var(--tray); border-radius: 0 0 18px 18px; overflow: hidden;
  }
  .window__product {
    position: absolute; left: 40px; top: 0; width: 583px; height: 270px;
    background: linear-gradient(180deg, #ddd8de 0%, #cfc2cb 45%, #b98f9f 75%, #7d3f52 100%);
    border-radius: 0 0 12px 12px;
  }
  .storage-badge {
    position: absolute; left: 98px; top: 749px; height: 41px; width: 184px;
    border: 2px solid #fff; border-radius: 21px; background: var(--blue);
    display: flex; align-items: center; gap: 8px; padding-left: 3px;
  }
  .storage-badge__icon {
    width: 35px; height: 35px; border-radius: 50%; background: var(--blue-light);
    border: 2px solid #fff; flex: none;
  }
  .storage-badge__text {
    font-family: "Barlow", sans-serif; font-weight: 700; font-size: 7.5px;
    line-height: 10px; color: #fff; text-transform: uppercase;
  }
</style>
</head>
<body>
<main class="canvas">
  <section class="pack">
    <div class="seal seal--top"></div>

    <div class="brand-tab">
      <span class="brand-tab__dot"></span>
      <span class="brand-tab__name">MAREN</span>
    </div>

    <h1 class="title">
      <span class="title__line">CUT</span>
      <span class="title__line">OCTOPUS</span>
    </h1>
    <p class="subtitle">TAKO SASHIMI</p>
    <p class="claim">The raw materials are caught in a very clean environment and processed in a modern factory with KVT certification. We are committed to additive-free products.</p>

    <div class="benefit-band">ALL NATURAL &bull; HIGHEST QUALITY &bull; TOP QUALITY</div>

    <div class="window">
      <div class="window__product" role="img" aria-label="Sliced cooked octopus tentacles visible through the clear window on a black tray"></div>
    </div>

    <div class="storage-badge">
      <svg class="storage-badge__icon" viewBox="0 0 36 36" aria-hidden="true">
        <g stroke="#fff" stroke-width="2" stroke-linecap="round">
          <line x1="18" y1="8" x2="18" y2="28"/>
          <line x1="9.3" y1="13" x2="26.7" y2="23"/>
          <line x1="9.3" y1="23" x2="26.7" y2="13"/>
        </g>
      </svg>
      <span class="storage-badge__text">Keep frozen, no preservatives<br>Net. wt 1 lb (500 g)</span>
    </div>

    <div class="seal seal--bottom"></div>
  </section>
</main>
</body>
</html>
```